Velmor Partners - website for real estate investment company

Create a bold, modern website that reflects Velmor’s success, professionalism, and credibility.
The design must stand out while maintaining a polished, corporate tone. (bold, but understated)
The client just created a new logo, and the website design must be in sync with the logo design. Information about the logo colors, fonts, and message are in the attached design brief.

Target Market(s)

b2b: banks, brokers, institutional partners, vendors, and property sellers.

Industry/Entity Type

real estate investment company

Number of Pages Required

1 page

Font styles to use
Sans Serif

Colors

Designer to choose colors to be used in the design.

Requirements
Must have
• 1. homepage design (psd) 2. a top banner image (psd) for a default inner page
Nice to have
• please see attached design brief
Should not have

```html
<!DOCTYPE html>
<html lang="en">
<head>
<meta charset="utf-8">
<title>Velmor Partners</title>
<link rel="stylesheet" href="https://fonts.googleapis.com/css2?family=Barlow:wght@600;700;800&family=Open+Sans:wght@400;600&display=swap">
<style>
:root{
  --red:#e01e26;
  --ink:#2d2d2d;
  --text:#555;
  --muted:#6b6b6b;
  --light:#ffffff;
  --header:#f7f7f7;
  --footer:#4b4b4e;
  --navy:#1f2a3b;
  --line:#d8d8d8;
}
*{box-sizing:border-box;margin:0;padding:0}
html,body{width:1200px;height:2735px;overflow:hidden}
body{position:relative;background:var(--light);font-family:"Open Sans",Arial,sans-serif;color:var(--ink)}
.abs{position:absolute}
.display{font-family:"Barlow",Arial,sans-serif;font-weight:800;text-transform:uppercase;letter-spacing:.3px}

/* header */
.site-header{position:absolute;left:0;top:0;width:1200px;height:74px;background:var(--header)}
.brand{left:144px;top:12px;font-family:"Barlow",Arial,sans-serif;font-weight:800;font-size:46px;line-height:50px;color:#3a3a3a;letter-spacing:1px}
.nav{left:389px;top:27px;display:flex;gap:30px;font-size:15px;color:#222}
.nav .active{color:var(--red)}

/* hero */
.hero{left:0;top:74px;width:1200px;height:694px;background:linear-gradient(180deg,#5d6168 0%,#7b7a72 35%,#8b7552 60%,#4d4a45 80%,#3c4148 100%)}
.hero-title-1{left:144px;top:162px;font-size:56px;line-height:64px;color:var(--red)}
.hero-title-2{left:144px;top:234px;font-size:56px;line-height:64px;color:var(--light)}
.hero-text{left:144px;top:307px;width:510px;font-size:18px;line-height:32px;font-weight:600;color:var(--light)}
.btn-outline{left:144px;top:501px;width:176px;height:51px;border:2px solid var(--light);color:var(--light);font-weight:600;font-size:16px;display:flex;align-items:center;justify-content:center}
.corner{position:absolute;left:0;top:0;width:0;height:0;border-top:18px solid var(--light);border-right:18px solid transparent}

/* feature cards */
.card{top:651px;width:296px;height:217px;background:var(--light);box-shadow:0 4px 14px rgba(0,0,0,.08);text-align:center}
.card svg{margin-top:22px}
.card h3{font-weight:400;font-size:18px;margin-top:6px;letter-spacing:.3px}
.card p{font-size:14px;line-height:24px;color:var(--muted);margin-top:8px;padding:0 16px}

/* about */
.about-frame{left:123px;top:929px;width:365px;height:294px;background:var(--red);clip-path:polygon(0 0,100% 0,94% 7%,7% 7%,7% 100%,0 100%)}
.photo{background:linear-gradient(135deg,#c9d7d8,#9aa6a8 45%,#5b5450 80%,#3b3633)}
.about-photo{left:144px;top:948px;width:454px;height:377px}
.about-title{left:666px;top:1002px;font-size:35px;line-height:42px;color:#3a3a3a}
.about-title span{color:var(--red)}
.about-text{left:663px;top:1057px;width:393px;font-size:14px;line-height:24px;color:var(--muted);text-align:justify}
.btn-red{left:663px;top:1216px;width:144px;height:44px;background:var(--red);color:var(--light);font-weight:600;font-size:14px;display:flex;align-items:center;justify-content:center}

/* stats */
.stats{left:0;top:1401px;width:1200px;height:236px;background:linear-gradient(110deg,#2a3446 0%,#1c2433 40%,#354258 60%,#1a2130 100%)}
.stat{top:67px;color:var(--light)}
.stat .num{font-family:"Barlow",Arial,sans-serif;font-weight:700;font-size:34px;line-height:40px}
.stat .bar{width:98px;height:3px;background:var(--red);margin:4px 0 12px}
.stat .label{font-size:14px}

/* portfolio */
.pf-title{left:144px;top:1706px;font-size:35px;line-height:49px;color:#3a3a3a}
.pf-title span{color:var(--red)}
.pf-text{left:660px;top:1713px;width:396px;font-size:14px;line-height:23.5px;color:#333;text-align:justify}
.side-photo{top:1900px;height:348px;opacity:.35;background:linear-gradient(135deg,#d8dcdc,#a4a39e 60%,#7d7a76)}
.pf-frame{left:193px;top:1835px;width:137px;height:135px;background:var(--red);clip-path:polygon(0 0,100% 0,92% 9%,9% 9%,9% 100%,0 100%)}
.pf-photo{left:205px;top:1847px;width:517px;height:348px;background:linear-gradient(135deg,#dbe8ec,#b9ccd2 40%,#6a6660 75%,#3d3a38)}
.pf-card{left:587px;top:2025px;width:365px;height:216px;background:var(--light);box-shadow:0 4px 16px rgba(0,0,0,.08);text-align:center}
.pf-card h4{font-weight:400;font-size:18px;line-height:29px;padding:15px 30px 13px;color:#222}
.pf-card hr{border:0;border-top:1px solid #e3e3e3;margin:0 12px}
.pf-card p{font-size:14px;line-height:23px;color:var(--muted);padding:12px 22px 8px}
.pf-card .more{color:var(--red);font-weight:600;font-size:14px;display:inline-flex;align-items:center;gap:8px}

.pager{left:378px;top:2288px;width:444px;height:20px;font-size:14px}
.pager .prev{position:absolute;left:0;top:0;color:#222}
.pager .next{position:absolute;right:0;top:0;color:var(--red)}
.track{position:absolute;left:96px;top:9px;width:273px;height:2px;background:#bbb}
.track i{position:absolute;left:0;top:-1px;width:80px;height:4px;background:var(--red)}
.count{left:0;top:2317px;width:1200px;text-align:center;font-weight:600;font-size:15px}
.count span{color:var(--red)}

/* footer */
.site-footer{left:0;top:2393px;width:1200px;height:342px;background:var(--footer);color:var(--light)}
.foot-brand{left:144px;top:60px;font-family:"Barlow",Arial,sans-serif;font-weight:800;font-size:58px;line-height:60px;letter-spacing:1px}
.contact{left:144px;font-size:16px;display:flex;align-items:center;gap:14px}
.copy{left:144px;top:310px;font-size:13px}
.touch{left:600px;top:58px;font-size:33px;line-height:40px}
.field{font-size:11px;font-weight:600}
.field-line{height:1px;background:#d0d0d0}
.btn-submit{left:602px;top:279px;width:454px;height:38px;background:var(--red);font-weight:600;font-size:14px;display:flex;align-items:center;justify-content:center}
</style>
</head>
<body>

<header class="site-header">
  <div class="abs brand">VELMOR</div>
  <nav class="abs nav">
    <span class="active">Home</span><span>Our Story</span><span>Investment Strategy</span><span>What Sets Us Apart</span><span>Our Portfolio</span><span>Contact</span>
  </nav>
</header>

<section class="abs hero" role="img" aria-label="City skyline across the water at sunset"></section>
<h1 class="abs display hero-title-1">Welcome to</h1>
<h1 class="abs display hero-title-2">Velmor Partners</h1>
<p class="abs hero-text">Velmor Partners Is A Vertically Integrated Real Estate Investment Firm With A Proven Four-decade Track Record. We Acquire, Reposition, and Operate High-performing Assets Across Multiple Sectors Always With A Focus On Exceptional, Risk-adjusted Returns.</p>
<a class="abs btn-outline"><span class="corner"></span>GET STARTED</a>

<div class="abs card" style="left:144px">
  <svg width="70" height="74" viewBox="0 0 70 74" fill="none" stroke="#e01e26" stroke-width="2.5"><circle cx="35" cy="32" r="28"/><circle cx="35" cy="32" r="19"/><path d="M28 36v-8h4l5-7c2 0 3 2 2 5h6c2 0 2 3 0 3 2 1 1 3 0 3 1 1 0 3-2 3H28z"/><path d="M22 56l-6 14 8-3 4 6 4-10M48 56l6 14-8-3-4 6-4-10"/></svg>
  <h3>EXPERIENCE</h3>
  <p>Lorem ipsum dolor sit amet, consectetur adipiscing elit, sed do</p>
</div>
<div class="abs card" style="left:452px">
  <svg width="70" height="74" viewBox="0 0 70 74" fill="none" stroke="#e01e26" stroke-width="2.5"><path d="M22 66h30M24 66l4-14h18l4 14M30 52c-6-8 0-14 6-20l-10 2-4-6 12-14 6-2c8 6 10 20 6 40"/><circle cx="38" cy="20" r="1.5"/><circle cx="12" cy="56" r="3"/><circle cx="60" cy="44" r="3"/><path d="M15 55l10-6M57 45l-8 2"/></svg>
  <h3>STRATEGY</h3>
  <p>Lorem ipsum dolor sit amet, consectetur adipiscing elit, sed do</p>
</div>
<div class="abs card" style="left:759px">
  <svg width="70" height="74" viewBox="0 0 70 74" fill="none" stroke="#e01e26" stroke-width="2.5"><path d="M20 44V34h8v10M32 44V26h8v18M44 44V18h8v26M16 28l14-10 8 6 16-14M48 8h7v7"/><path d="M4 56c16-16 46-16 62 0-16 16-46 16-62 0z"/><circle cx="35" cy="56" r="7"/></svg>
  <h3>VISION</h3>
  <p>Lorem ipsum dolor sit amet, consectetur adipiscing elit, sed do</p>
</div>

<div class="abs about-frame"></div>
<div class="abs photo about-photo" role="img" aria-label="Team of colleagues meeting around a laptop in an office"></div>
<h2 class="abs display about-title"><span>About</span> Velmor Partners</h2>
<p class="abs about-text">Velmor Partners is a real estate investment company that has been successfully buying, improving, and managing properties for over 40 years. We focus on making smart investments in different types of real estate to deliver strong, reliable returns while carefully managing risk.</p>
<a class="abs btn-red"><span class="corner"></span>READ MORE</a>

<section class="abs stats" role="img" aria-label="Dark view of glass office towers looking upward">
  <div class="abs stat" style="left:144px;top:73px">
    <svg width="78" height="78" viewBox="0 0 78 78" fill="none" stroke="#fff" stroke-width="3"><path d="M4 22L39 4l35 18zM8 22h62v6H8zM14 28v34M26 28v34M38 28v34M50 28v34M62 28v34M6 64h66v6H6z"/></svg>
  </div>
  <div class="abs stat" style="left:247px">
    <div class="num">1989</div><div class="bar"></div><div class="label">Founded</div>
  </div>
  <div class="abs stat" style="left:402px;top:73px">
    <svg width="74" height="78" viewBox="0 0 74 78" fill="none" stroke="#fff" stroke-width="3"><path d="M37 22c-8-6-14-12-8-17 4-3 8 0 8 3 0-3 4-6 8-3 6 5 0 11-8 17z"/><circle cx="26" cy="34" r="5"/><circle cx="48" cy="34" r="5"/><circle cx="37" cy="42" r="5"/><path d="M4 40v20l18 14h14V60L20 48M70 40v20L52 74H38V60l16-12"/></svg>
  </div>
  <div class="abs stat" style="left:503px">
    <div class="num">23,000+</div><div class="bar"></div><div class="label">Multifamily &amp; Healthcare Units</div>
  </div>
  <div class="abs stat" style="left:758px;top:73px">
    <svg width="72" height="78" viewBox="0 0 72 78" fill="none" stroke="#fff" stroke-width="3"><path d="M14 40V12h22v28M36 26h22v22M44 4v10M52 4v10M60 4v10"/><circle cx="40" cy="50" r="10"/><path d="M2 58h16l14 8h24l12-8v12H40l-22 6H2"/></svg>
  </div>
  <div class="abs stat" style="left:857px">
    <div class="num">$300+</div><div class="bar"></div><div class="label">Million Invested In Renovations</div>
  </div>
</section>

<h2 class="abs display pf-title">Our <span>Portfolio</span><br>Highlights</h2>
<p class="abs pf-text">Duis aute irure dolor in reprehenderit in voluptate velit esse cillum dolore eu fugiat nulla pariatur excepteur sint occaecat cupidatat non proident, sunt in culpa qui officia</p>

<div class="abs side-photo" style="left:0;width:154px" role="img" aria-label="Colleagues discussing at a table"></div>
<div class="abs side-photo" style="left:1011px;width:189px" role="img" aria-label="Businessman reviewing a document"></div>
<div class="abs pf-frame"></div>
<div class="abs pf-photo" role="img" aria-label="Business team in discussion at an office table"></div>
<article class="abs pf-card">
  <h4>Powering The Transition To Solar Energy Infrastructure</h4>
  <hr>
  <p>Duis aute irure dolor in reprehenderit in voluptate velit esse cillum dolore eu fugiat nulla</p>
  <a class="more">VIEW MORE <svg width="16" height="12" viewBox="0 0 16 12" fill="none" stroke="#e01e26" stroke-width="1.8"><path d="M0 6h14M9 1l5 5-5 5"/></svg></a>
</article>

<div class="abs pager">
  <span class="prev">‹ &nbsp;&nbsp;&nbsp;&nbsp; Previous</span>
  <span class="track"><i></i></span>
  <span class="next">Next &nbsp;&nbsp;&nbsp;&nbsp; ›</span>
</div>
<div class="abs count"><span>1</span> / 4</div>

<footer class="abs site-footer">
  <div class="abs foot-brand">VELMOR</div>
  <div class="abs contact" style="top:146px">
    <svg width="14" height="14" viewBox="0 0 14 14" fill="#fff"><path d="M3 0l3 3-2 2c1 2 3 4 5 5l2-2 3 3-2 3C6 14 0 8 0 2z"/></svg>(555) 014-2290</div>
  <div class="abs contact" style="top:185px">
    <svg width="14" height="11" viewBox="0 0 14 11" fill="#fff"><path d="M0 0h14v2L7 6 0 2zM0 3.5l7 4 7-4V11H0z"/></svg>info@velmorpartners.com</div>
  <div class="abs contact" style="top:225px">
    <svg width="10" height="14" viewBox="0 0 10 14" fill="#fff"><path d="M5 0a5 5 0 015 5c0 4-5 9-5 9S0 9 0 5a5 5 0 015-5zm0 3a2 2 0 100 4 2 2 0 000-4z"/></svg>2140 Harbor Rd, Lakeview, NJ 08800</div>
  <div class="abs copy">© 2025 Velmor Partners &nbsp;|&nbsp; All Rights Reserved</div>

  <h2 class="abs display touch">Get in Touch</h2>
  <div class="abs field" style="left:601px;top:125px">Name *</div>
  <div class="abs field-line" style="left:602px;top:152px;width:213px"></div>
  <div class="abs field" style="left:842px;top:125px">Email *</div>
  <div class="abs field-line" style="left:843px;top:152px;width:213px"></div>
  <div class="abs field" style="left:601px;top:184px">Message *</div>
  <div class="abs field-line" style="left:602px;top:250px;width:454px"></div>
  <a class="abs btn-submit"><span class="corner"></span>SUBMIT NOW</a>
</footer>

</body>
</html>
```